Design for a 4 screens mobile app: Brightnook

The app is a compact but illustrated phone/address book...
We need a design for the 5 screens of the app (see screens attached):
a) "index" : 1 screen with 6 pictures of contact person
b) "contact list" : 1 screen, to manage (add/del/edit) the contacts of the phone/address book
c) "add contact" : 1 screen to add a contact (a picture + a phone number)
d) "update contact" : similar to "add"
e) "fields missing" : add/edit screens in "error" state
We also need the ico design + loading screen.
No specific guidelines, nor logo or whatever.
It will be a free app distributed on iOS and Androïd.
We just want to make it looking nice & very usable for end users.
B2C

```html
<!DOCTYPE html>
<html lang="en">
<head>
<meta charset="utf-8">
<title>Brightnook – Contact Detail</title>
<link href="https://fonts.googleapis.com/css2?family=Roboto:wght@400;500&display=swap" rel="stylesheet">
<style>
  :root {
    --status-blue: #1c3d68;
    --bar-blue: #234f84;
    --white: #ffffff;
    --ink: #222222;
    --label: #444444;
    --muted: #a9a9a9;
    --icon-grey: #9e9e9e;
    --divider: #e6e6e6;
    --call-green: #3dbb3f;
    --accent-yellow: #fdd22c;
  }
  * { margin: 0; padding: 0; box-sizing: border-box; }
  html, body { width: 675px; height: 1200px; overflow: hidden; background: var(--white); }
  body { font-family: 'Roboto', sans-serif; position: relative; }

  .status-bar {
    position: absolute; left: 0; top: 0; width: 675px; height: 45px;
    background: var(--status-blue); color: var(--white);
  }
  .status-bar .signal { position: absolute; left: 523px; top: 13px; }
  .status-bar .battery { position: absolute; left: 566px; top: 11px; }
  .status-bar .clock { position: absolute; left: 596px; top: 10px; font-size: 23px; }

  .app-bar {
    position: absolute; left: 0; top: 45px; width: 675px; height: 105px;
    background: var(--bar-blue); box-shadow: 0 3px 6px rgba(0,0,0,0.25); z-index: 2;
  }
  .app-bar .back { position: absolute; left: 34px; top: 36px; }
  .app-bar .title {
    position: absolute; left: 105px; top: 32px; color: var(--white);
    font-size: 34px; font-weight: 400;
  }

  .avatar {
    position: absolute; left: 227px; top: 206px; width: 220px; height: 220px; border-radius: 50%;
    background: radial-gradient(circle at 50% 40%, #e9d3c2 0%, #b7714a 55%, #6d3a22 100%);
  }
  .photo-action { position: absolute; left: 98px; top: 298px; }
  .settings-action { position: absolute; left: 537px; top: 291px; }
  .contact-name {
    position: absolute; left: 0; top: 465px; width: 675px; text-align: center;
    font-size: 35px; color: var(--ink);
  }

  .phone-entry { position: absolute; left: 0; width: 675px; height: 135px; }
  .phone-entry.work { top: 578px; }
  .phone-entry.home { top: 714px; }
  .phone-entry .kind { position: absolute; left: 100px; top: 10px; font-size: 28px; color: var(--label); }
  .phone-entry .number { position: absolute; left: 100px; top: 64px; font-size: 29px; color: var(--muted); }
  .phone-entry .actions { position: absolute; left: 510px; top: 22px; display: flex; gap: 12px; }
  .round-btn { width: 50px; height: 50px; border-radius: 50%; display: flex; align-items: center; justify-content: center; }
  .round-btn.call { background: var(--call-green); }
  .round-btn.message { background: var(--accent-yellow); }
  .divider { position: absolute; left: 100px; top: 702px; width: 575px; height: 1px; background: var(--divider); }

  .add-contact-fab {
    position: absolute; left: 520px; top: 1033px; width: 112px; height: 112px; border-radius: 50%;
    background: var(--accent-yellow); box-shadow: 0 4px 10px rgba(0,0,0,0.25);
    display: flex; align-items: center; justify-content: center;
  }
</style>
</head>
<body>
  <div class="status-bar">
    <svg class="signal" width="22" height="22" viewBox="0 0 22 22"><path d="M22 0 V22 H0 Z" fill="var(--white)"/></svg>
    <svg class="battery" width="14" height="24" viewBox="0 0 14 24"><rect x="4" y="0" width="6" height="3" fill="var(--white)"/><rect x="0" y="2" width="14" height="22" rx="1" fill="var(--white)"/></svg>
    <span class="clock">12:30</span>
  </div>

  <header class="app-bar">
    <svg class="back" width="32" height="32" viewBox="0 0 24 24"><path d="M20 11H7.8l5.6-5.6L12 4l-8 8 8 8 1.4-1.4L7.8 13H20z" fill="var(--white)"/></svg>
    <h1 class="title">Contact Detail</h1>
  </header>

  <svg class="photo-action" width="38" height="38" viewBox="0 0 24 24"><path d="M21 19V5a2 2 0 0 0-2-2H5a2 2 0 0 0-2 2v14a2 2 0 0 0 2 2h14a2 2 0 0 0 2-2zM8.5 13.5l2.5 3 3.5-4.5 4.5 6H5z" fill="var(--icon-grey)"/></svg>
  <div class="avatar" role="img" aria-label="Contact portrait photo"></div>
  <svg class="settings-action" width="40" height="40" viewBox="0 0 24 24"><path d="M19.4 13a7.5 7.5 0 0 0 0-2l2.1-1.6-2-3.5-2.5 1a7.4 7.4 0 0 0-1.7-1L14.9 3h-4l-.4 2.9a7.4 7.4 0 0 0-1.7 1l-2.5-1-2 3.5L6.4 11a7.5 7.5 0 0 0 0 2l-2.1 1.6 2 3.5 2.5-1a7.4 7.4 0 0 0 1.7 1l.4 2.9h4l.4-2.9a7.4 7.4 0 0 0 1.7-1l2.5 1 2-3.5zM12.9 15.5a3.5 3.5 0 1 1 0-7 3.5 3.5 0 0 1 0 7z" fill="var(--icon-grey)"/></svg>

  <h2 class="contact-name">Add A Name</h2>

  <section class="phone-entry work">
    <span class="kind">Work</span>
    <span class="number">555-210-4837</span>
    <div class="actions">
      <span class="round-btn call"><svg width="26" height="26" viewBox="0 0 24 24"><path d="M6.6 10.8a15.1 15.1 0 0 0 6.6 6.6l2.2-2.2c.3-.3.7-.4 1-.2 1.1.4 2.3.6 3.6.6.6 0 1 .4 1 1V20c0 .6-.4 1-1 1A17 17 0 0 1 3 4c0-.6.4-1 1-1h3.5c.6 0 1 .4 1 1 0 1.3.2 2.5.6 3.6.1.3 0 .7-.2 1z" fill="var(--white)"/></svg></span>
      <span class="round-btn message"><svg width="24" height="24" viewBox="0 0 24 24"><path d="M20 2H4a2 2 0 0 0-2 2v18l4-4h14a2 2 0 0 0 2-2V4a2 2 0 0 0-2-2zM9 11H7V9h2zm4 0h-2V9h2zm4 0h-2V9h2z" fill="var(--white)"/></svg></span>
    </div>
  </section>
  <div class="divider"></div>
  <section class="phone-entry home">
    <span class="kind">Home</span>
    <span class="number">555-268-1093</span>
    <div class="actions">
      <span class="round-btn call"><svg width="26" height="26" viewBox="0 0 24 24"><path d="M6.6 10.8a15.1 15.1 0 0 0 6.6 6.6l2.2-2.2c.3-.3.7-.4 1-.2 1.1.4 2.3.6 3.6.6.6 0 1 .4 1 1V20c0 .6-.4 1-1 1A17 17 0 0 1 3 4c0-.6.4-1 1-1h3.5c.6 0 1 .4 1 1 0 1.3.2 2.5.6 3.6.1.3 0 .7-.2 1z" fill="var(--white)"/></svg></span>
      <span class="round-btn message"><svg width="24" height="24" viewBox="0 0 24 24"><path d="M20 2H4a2 2 0 0 0-2 2v18l4-4h14a2 2 0 0 0 2-2V4a2 2 0 0 0-2-2zM9 11H7V9h2zm4 0h-2V9h2zm4 0h-2V9h2z" fill="var(--white)"/></svg></span>
    </div>
  </section>

  <div class="add-contact-fab">
    <svg width="52" height="52" viewBox="0 0 24 24"><circle cx="10" cy="8" r="4" fill="var(--white)"/><path d="M2 21c0-4.4 3.6-7 8-7s8 2.6 8 7z" fill="var(--white)"/><path d="M19 2v3h3v1.6h-3v3h-1.6v-3h-3V5h3V2z" fill="var(--white)"/></svg>
  </div>
</body>
</html>
```